GownLoom.com will be an online bespoke garment creator, specifically around designing your own Wedding Dress. It will enable you to specify your own material, colours and patterns and customized features such as bows, sequins, diamantes, and more from a selection of per-defined base garments and customize them to your taste.
The concept is similar to:
www.threadwellstudio.com
But the design should reflect more like
www.velmarrow.com
www.pindle.com - (in particular the build elements)
www.korvo.com
It will be aimed at the Female marketplace. However this does not mean to use pink or portray the brand in very girly way. It should use good white space, and look very classy. not too busy, but functional and elegant, with a focus on stable and responsible site that will deliver. A wedding dress is an important purchase and to trust a company to make one for you from a distance takes a lot of trust from the customer perspective.
We want to first create the homepage and "build the dress" pages, which will consist of Enter your Measurements, Choose a Base Silhouette Style, Choose Fabric, Choose Colors, Customize Dress, Summary, Order Page, Thank you Page.
It will then have generic About us, How to Measure, Agent Locator, How it works, Contact, Order Samples, Support.
A very basic wire frame was created here to aid development, but the branding is being developed, so do not use any of it for inspiration just a visual interpretation - http://pageyard4.info/bespoke/
The link above is merely an idea on what areas the site will have. The actual design and colour scheme should reflect these sites.
The branding is also here - www.gownloom.com not the one used within that link.
The site will enable you to log in, save your designs and your delivery and measurement information. It will also offer the usual social media buttons to share the design and ability to leave comments.
This will be the first draft and the winning design will get to design the other pages and future work associated to the site.
thanks!

```html
<!DOCTYPE html>
<html lang="en">
<head>
<meta charset="utf-8">
<title>GownLoom – Home</title>
<link rel="stylesheet" href="https://fonts.googleapis.com/css2?family=Source+Sans+3:wght@400;600&family=Arimo:wght@400&display=swap">
<style>
:root{
  --ink:#222;
  --text:#555;
  --muted:#777;
  --line:#c9c9c9;
  --panel:#f1f1f1;
  --bar:#d6d6d6;
  --dark:#1a1a1a;
  --blue:#1f5c9e;
  --red:#b3121b;
  --active:#777;
}
*{box-sizing:border-box;margin:0;padding:0}
html,body{width:800px;height:1200px;overflow:hidden;background:#fff}
body{position:relative;font-family:"Source Sans 3",sans-serif;color:var(--text)}
.abs{position:absolute}
.header-sky{left:0;top:0;width:800px;height:90px;background:linear-gradient(#eef0f3,#fff)}
.brand{left:20px;top:20px;display:flex;align-items:center;gap:10px}
.brand-mark{width:48px;height:48px;border-radius:50%;border:3px solid var(--dark);background:#fff}
.brand-name{font-size:27px;color:var(--dark);letter-spacing:.3px}
.phone{left:380px;top:30px;display:flex;align-items:center;gap:6px;font-size:15px;color:#555}
.toplinks{right:24px;top:14px;font-size:11px;color:#666}
.toplinks span{margin:0 5px;color:#999}
.search{left:625px;top:48px;width:150px;height:20px;border:1px solid var(--line);border-radius:10px;background:#fff;font-size:8px;color:#777;padding:5px 12px}
.search svg{position:absolute;right:8px;top:4px}
.nav{left:16px;top:92px;width:766px;height:31px;border:1px solid #aaa;display:flex;background:#fff}
.nav a{font-size:11.5px;color:var(--ink);text-decoration:none;display:flex;align-items:center;padding:0 13px;border-right:1px solid #bbb}
.nav a.active{background:var(--active);color:#fff}
.nav a:last-child{border-right:none}
.slider{left:16px;top:135px;width:766px;height:292px;border:1px solid #e2e2e2;background:#fff;box-shadow:0 4px 6px rgba(0,0,0,.08)}
.slide{left:31px;top:143px;width:740px;height:273px;background:linear-gradient(100deg,#e5e6df 0%,#b9bda0 25%,#dcd7cc 55%,#c7a98b 72%,#ebe9e6 100%)}
.dots{left:356px;top:417px;display:flex;gap:4px}
.dots i{width:8px;height:8px;border-radius:50%;background:#888;display:block}
.dots i.on{background:#9acd32}
.arrow{top:255px;width:16px;height:32px;background:#444;display:flex;align-items:center;justify-content:center}
.arrow.l{left:0;border-radius:0 16px 16px 0}
.arrow.r{right:0;border-radius:16px 0 0 16px}
.card{width:228px;height:158px;top:465px}
.card-head{height:32px;background:linear-gradient(#e4e4e4,#c9c9c9);font-size:14.5px;color:var(--ink);padding:7px 12px}
.card-body{position:relative;height:126px;border:1px solid #ddd;border-top:none;background:linear-gradient(#fff,#f3f3f3)}
.card-photo{position:absolute;left:10px;top:12px;width:112px;height:73px;border:2px solid #eee}
.card-text{position:absolute;left:130px;top:18px;font-size:10.5px;line-height:19px;color:#555}
.btn{position:absolute;right:8px;bottom:6px;height:22px;padding:0 17px;background:var(--dark);color:#fff;font-size:11px;border-radius:3px;display:flex;align-items:center}
.welcome{left:25px;top:666px;width:494px}
.welcome h1{font-weight:400;font-size:15px;color:var(--blue);margin-bottom:10px}
.welcome p{font-size:8.6px;line-height:19.2px;color:#555;margin-bottom:19px}
.more{font-size:8.5px;color:var(--red)}
.testimonials{left:548px;top:650px;width:242px;height:252px;background:#f7f7f7}
.testimonials h2{font-weight:400;font-size:14.5px;color:var(--ink);background:#e6e6e6;padding:6px 17px;margin:5px 6px 0 6px;height:28px}
.quote{position:absolute;left:20px;width:220px}
.quote-photo{position:absolute;left:0;top:0;width:56px;height:52px;border:2px solid #e6e6e6}
.quote p{margin-left:67px;font-size:8.8px;line-height:16px;color:#666}
.quote b{display:block;font-weight:400;font-size:10.5px;color:var(--ink);margin:2px 0 0 71px}
.rule{left:0;top:916px;width:800px;border-top:1px dotted #888}
.fcol{top:940px}
.fcol h3{font-family:"Arimo",sans-serif;font-weight:400;font-size:11.5px;color:#333;margin-bottom:17px}
.fcol li{list-style:none;font-family:"Arimo",sans-serif;font-size:8.3px;color:#777;line-height:14.4px}
.newsletter{left:587px;top:940px}
.newsletter h3{font-weight:400;font-size:12px;color:#222;margin-bottom:10px}
.nl-form{display:flex;width:185px;height:24px;border:1px solid #999;border-radius:3px;overflow:hidden}
.nl-form span{flex:1;font-size:7.5px;color:#444;padding:7px 10px}
.nl-form em{font-style:normal;background:#555;color:#fff;font-size:10px;padding:6px 7px}
.hours{left:595px;top:1016px;font-family:"Arimo",sans-serif}
.hours h3{font-weight:400;font-size:11.5px;color:#333;margin-bottom:10px}
.hours p{font-size:8.3px;color:#777;line-height:14.4px}
.glow{left:200px;top:1088px;width:420px;height:10px;background:radial-gradient(ellipse,rgba(0,0,0,.08),transparent 70%)}
.pay{left:24px;top:1128px;display:flex;gap:10px}
.pay span{width:34px;height:19px;border:1px solid #ccc;font-family:"Arimo",sans-serif;font-size:6.5px;color:#333;display:flex;align-items:center;justify-content:center}
.social{right:20px;top:1126px;display:flex;gap:8px}
.social span{display:flex;flex-direction:column;align-items:center;font-family:"Arimo",sans-serif;font-size:6px;color:#666;gap:1px}
.social i{width:18px;height:18px;border-radius:50%;background:#6f8fb0;display:block}
.copy{right:18px;top:1155px;font-family:"Arimo",sans-serif;font-size:9.5px;color:#333}
</style>
</head>
<body>
<div class="abs header-sky"></div>

<div class="abs brand">
  <div class="brand-mark"></div>
  <div class="brand-name">GOWNLOOM</div>
</div>

<div class="abs phone">
  <svg width="20" height="26" viewBox="0 0 20 26"><path d="M5 1 L9 6 L6 9 Q8 15 13 19 L16 16 L20 21 L16 25 Q6 22 2 9 Q1 4 5 1Z" fill="#333"/></svg>
  1800 555 0199
</div>

<div class="abs toplinks">My Account<span>|</span>Manage Order<span>|</span>Order Status<span>|</span>Login</div>

<div class="abs search">Search
  <svg width="14" height="12" viewBox="0 0 14 12"><circle cx="5" cy="5" r="4" fill="none" stroke="#999" stroke-width="1.5"/><line x1="8" y1="8" x2="13" y2="11" stroke="#999" stroke-width="2"/></svg>
</div>

<nav class="abs nav">
  <a class="active">ABOUT US</a><a>HOW TO MEASURE</a><a>AGENT LOCATOR</a><a>HOW IT WORKS</a><a>CONTACT</a><a>ORDER SAMPLES</a><a>SUPPORT</a>
</nav>

<div class="abs slider"></div>
<div class="abs slide" role="img" aria-label="Bride in a white gown beside a bouquet of white roses"></div>
<div class="abs dots"><i></i><i></i><i class="on"></i><i></i><i></i></div>
<div class="abs arrow l"><svg width="8" height="10"><path d="M6 1 L2 5 L6 9" stroke="#fff" stroke-width="2" fill="none"/></svg></div>
<div class="abs arrow r"><svg width="8" height="10"><path d="M2 1 L6 5 L2 9" stroke="#fff" stroke-width="2" fill="none"/></svg></div>

<section class="abs card" style="left:20px">
  <div class="card-head">Create Gown</div>
  <div class="card-body">
    <div class="card-photo" role="img" aria-label="Designer with dress forms" style="background:linear-gradient(90deg,#cfc7bd,#eae6df,#6b5b5b)"></div>
    <div class="card-text">Create your Fabulous<br>Design Gown by<br>Create Now button</div>
    <div class="btn">Create Now</div>
  </div>
</section>
<section class="abs card" style="left:285px">
  <div class="card-head">Measure yourself</div>
  <div class="card-body">
    <div class="card-photo" role="img" aria-label="Bride being measured for a gown" style="background:linear-gradient(90deg,#9aa3ad,#e9e7e1,#d8c9b5)"></div>
    <div class="card-text">Create your Fabulous<br>Design Gown by<br>Create Now button</div>
    <div class="btn">Measure Now</div>
  </div>
</section>
<section class="abs card" style="left:550px">
  <div class="card-head">Agent Locator</div>
  <div class="card-body">
    <div class="card-photo" role="img" aria-label="Agent in a bridal showroom" style="background:linear-gradient(90deg,#2c3b55,#5d7a4f,#dcdfe2)"></div>
    <div class="card-text">Create your Fabulous<br>Design Gown by<br>Create Now button</div>
    <div class="btn">Find Agent</div>
  </div>
</section>

<section class="abs welcome">
  <h1>Welcome to GownLoom</h1>
  <p>Nunc varius facilisis eros. Sed erat. In in velit quis arcu ornare laoreet. Nunc varius facilisis eros. Sed erat. In in velit quis arcu ornare laoreet. Nunc varius facilisis eros. Sed erat. In in velit quis arcu ornare laoreet. Nunc varius facilisis eros. Sed erat. In in velit quis arcu ornare laoreet. Nunc varius facilisis eros. Sed erat. In in velit quis arcu ornare laoreet. Nunc varius facilisis eros. Sed erat. In in velit quis arcu ornare laoreet. Nunc varius facilisis eros. Sed erat.</p>
  <p>In in velit quis arcu ornare laoreet. Nunc varius facilisis eros. Sed erat. In in velit quis arcu ornare laoreet. Nunc varius facilisis eros. Sed erat. In in velit quis arcu ornare laoreet. Nunc varius facilisis eros. Sed erat. In in velit quis arcu ornare laoreet. Nunc varius facilisis eros. Sed erat. In in velit quis arcu ornare laoreet. Nunc varius facilisis eros. Sed erat. In in velit quis arcu ornare laoreet. Nunc varius facilisis eros. Sed erat. In in velit quis arcu ornare laoreet.</p>
</section>
<div class="abs more" style="left:469px;top:872px">View More &nbsp;&gt;&gt;</div>

<aside class="abs testimonials">
  <h2>Testimonials</h2>
  <div class="quote" style="top:55px">
    <div class="quote-photo" role="img" aria-label="Portrait of a bride" style="background:linear-gradient(#c9b79c,#e8e2d6)"></div>
    <p>None of the other companies has the result we do. So stick to the best that's how you will be the best don't opt for the second best.</p>
    <b>Clara</b>
  </div>
  <div style="position:absolute;left:12px;top:144px;width:228px;border-top:1px solid #ddd"></div>
  <div class="quote" style="top:160px">
    <div class="quote-photo" role="img" aria-label="Portrait of a smiling bride" style="background:linear-gradient(#3a2f2a,#b08c72)"></div>
    <p>None of the other companies has the result we do. So stick to the best that's how you will be the best don't opt for the second best.</p>
    <b>Renata</b>
  </div>
</aside>
<div class="abs more" style="left:724px;top:894px">View More &nbsp;&gt;&gt;</div>

<div class="abs rule"></div>

<div class="abs fcol" style="left:33px"><h3>ABOUT US</h3><ul><li>Home</li><li>About us</li><li>Testimonials</li><li>Contact Us</li><li>Sitemap</li></ul></div>
<div class="abs fcol" style="left:154px"><h3>INFORMATION</h3><ul><li>Blog</li><li>FAQs</li><li>News</li><li>Terms &amp; Conditions</li><li>Provacy Policy</li></ul></div>
<div class="abs fcol" style="left:307px"><h3>MYACCOUNT</h3><ul><li>Manage Order</li><li>Order History</li><li>Order Status</li><li>Shipping Status</li><li>Help Support</li></ul></div>
<div class="abs fcol" style="left:443px"><h3>PRODUCT</h3><ul><li>Overview</li><li>Gown Styles</li><li>Agent Locator</li><li>Measure Yourself</li><li>Style Guide</li></ul></div>

<div class="abs newsletter">
  <h3>Sign up For Our Newsletter</h3>
  <div class="nl-form"><span>Enter your email address</span><em>SUBMIT</em></div>
</div>
<div class="abs hours">
  <h3>OPENING TIME :</h3>
  <p>MON - FRI : &nbsp;&nbsp;8.00 to 18.00</p>
  <p>&nbsp;&nbsp;&nbsp;&nbsp;&nbsp;&nbsp;&nbsp;&nbsp;&nbsp;&nbsp;&nbsp;SAT : &nbsp;&nbsp;9.00 to 18.00</p>
  <p>&nbsp;&nbsp;&nbsp;&nbsp;&nbsp;&nbsp;&nbsp;&nbsp;&nbsp;&nbsp;&nbsp;SUN : &nbsp;&nbsp;10.00 to 18.00</p>
</div>

<div class="abs glow"></div>

<div class="abs pay"><span>Payvine</span><span>Dyscard</span><span>Vanta</span><span>Amtrex</span><span>Meridia</span><span>Mestra</span></div>
<div class="abs social">
  <span><i></i>Friendly</span><span><i></i>Chirper</span><span><i></i>Linkly</span><span><i></i>Feedo</span>
</div>
<div class="abs copy">© 2012 gownloom, All Rights Reserved</div>
</body>
</html>
```